Content marketing firm needs a creative out of the box stationary design

Please take a look to the uploaded logo
I need the whole stationary package which include designs for (business card, letterhead, folder, notepad, company profile, small and big envelop, CD and its cover, key medal, header cover for social media pages "facebook, twitter, linkedin, insgram, google+" and website, favicon for website, E-mail signature, flyer, brochure)

```html
<!DOCTYPE html>
<html lang="en">
<head>
<meta charset="utf-8">
<title>Garnet Words — Stationery Set</title>
<link rel="stylesheet" href="https://fonts.googleapis.com/css2?family=Open+Sans:wght@400;600;700;800&display=swap">
<style>
  :root{
    --backdrop:#45464b;
    --brand-blue:#29abe2;
    --paper:#ffffff;
    --ink:#1d1d1f;
    --ink-soft:#6b6b6b;
    --disc-grey:#6d6e71;
  }
  *{box-sizing:border-box;margin:0;padding:0}
  html,body{width:1200px;height:1000px;overflow:hidden}
  body{background:var(--backdrop);font-family:"Open Sans",Arial,sans-serif;color:var(--ink);position:relative}
  .piece{position:absolute;background:var(--paper);overflow:hidden}
  .corner{position:absolute;width:0;height:0}
  .wordmark{font-weight:800;color:var(--ink);text-transform:uppercase;line-height:1;text-align:center;letter-spacing:.02em}

  /* Envelope back */
  .envelope-back{left:85px;top:277px;width:315px;height:157px}
  .envelope-back svg{position:absolute;left:0;top:0}

  /* Envelope front */
  .envelope-front{left:85px;top:452px;width:315px;height:158px}
  .envelope-front .corner{right:0;top:0;border-top:22px solid var(--brand-blue);border-left:22px solid transparent}
  .envelope-front .wordmark{position:absolute;left:12px;top:24px;font-size:8px;text-align:left}
  .envelope-front .sender{position:absolute;left:55px;top:16px;font-size:5px;line-height:8px;color:var(--ink-soft)}
  .envelope-front .recipient{position:absolute;left:132px;top:67px;font-size:5.5px;line-height:8px;color:var(--ink)}
  .footer-band{position:absolute;left:0;bottom:0;width:100%;height:17px;background:var(--brand-blue);color:#fff;font-size:5.5px;display:flex;align-items:center;padding-left:15px}
  .footer-band span:nth-child(1){width:97px}
  .footer-band span:nth-child(2){width:84px}

  /* Business cards */
  .card-front{left:83px;top:629px;width:133px;height:75px}
  .card-front .corner{left:0;top:0;border-top:22px solid var(--brand-blue);border-right:22px solid transparent}
  .card-front .wordmark{position:absolute;left:0;width:100%;top:30px;font-size:9px}
  .card-back{left:267px;top:629px;width:133px;height:75px;background:var(--brand-blue);color:#fff}
  .card-back .corner{right:0;top:0;border-top:18px solid var(--paper);border-left:18px solid transparent}
  .card-back .holder-name{position:absolute;left:10px;top:20px;font-size:6px;font-weight:600;letter-spacing:.03em}
  .card-back .holder-details{position:absolute;left:10px;top:38px;font-size:3.8px;line-height:6px}
  .card-back .mark-square{position:absolute;left:88px;top:24px;width:28px;height:28px;border:2px solid #fff}

  /* Letterhead */
  .letterhead-underlay{position:absolute;left:483px;top:290px;width:313px;height:443px;background:var(--brand-blue)}
  .letterhead{left:514px;top:259px;width:314px;height:445px}
  .letterhead .corner-top{left:0;top:0;border-top:35px solid var(--brand-blue);border-right:35px solid transparent}
  .letterhead .corner-bottom{right:0;bottom:0;border-bottom:35px solid var(--brand-blue);border-left:35px solid transparent}
  .letterhead .wordmark{position:absolute;left:0;width:100%;top:40px;font-size:9px}
  .letterhead .sender{position:absolute;left:18px;top:83px;font-size:6px;line-height:9px;color:var(--ink-soft)}
  .letterhead .body{position:absolute;left:18px;top:137px;width:282px;font-size:5.6px;line-height:8.6px;color:var(--ink-soft)}
  .letterhead .body p{margin-bottom:7px}
  .letterhead .body .salutation{margin-bottom:8px}
  .letterhead .signer{position:absolute;left:18px;top:314px;font-size:6.5px;font-weight:700}
  .letterhead .signature{position:absolute;left:18px;top:325px;width:82px;height:22px;background:#eeeeee}
  .letterhead .footer{position:absolute;left:18px;top:424px;font-size:6px;color:var(--brand-blue);display:flex}
  .letterhead .footer span:nth-child(1){width:68px}
  .letterhead .footer span:nth-child(2){width:101px}

  /* CD */
  .disc{position:absolute;left:889px;top:234px;width:222px;height:222px}
  .disc .wordmark{position:absolute;left:0;width:100%;top:42px;font-size:17px}

  /* CD sleeve */
  .sleeve{left:871px;top:490px;width:263px;height:245px}
  .sleeve .top-rule{position:absolute;left:0;top:0;width:100%;height:7px;background:var(--brand-blue)}
  .sleeve .bottom-band{position:absolute;left:0;bottom:0;width:100%;height:17px;background:var(--brand-blue)}
  .sleeve .wordmark{position:absolute;left:0;width:100%;top:150px;font-size:20px;line-height:1.1}
</style>
</head>
<body>

  <!-- Envelope, flap side -->
  <section class="piece envelope-back" aria-label="Envelope back">
    <svg width="315" height="157" viewBox="0 0 315 157">
      <path d="M0 0 H315 V16 Q315 34 298 34 H17 Q0 34 0 16 Z" fill="var(--brand-blue)"/>
    </svg>
  </section>

  <!-- Envelope, address side -->
  <section class="piece envelope-front" aria-label="Envelope front">
    <span class="corner"></span>
    <div class="wordmark">Garnet<br>Words</div>
    <div class="sender">Alder Lane<br>Brookmere Court 12-408<br>7134620</div>
    <div class="recipient">Tobias Lennard Frey<br>Blk 218 Hollowmere Row<br>#03-117 Westvale</div>
    <div class="footer-band"><span>Company Address</span><span>hello@garnetwords.com</span><span>5550-3142</span></div>
  </section>

  <!-- Business cards -->
  <section class="piece card-front" aria-label="Business card front">
    <span class="corner"></span>
    <div class="wordmark">Garnet<br>Words</div>
  </section>
  <section class="piece card-back" aria-label="Business card back">
    <span class="corner"></span>
    <div class="holder-name">CLARA VOSTELL</div>
    <div class="holder-details"><strong>Manager</strong><br>Corvell House<br>hello@garnetwords.com<br>5550-3142</div>
    <span class="mark-square"></span>
  </section>

  <!-- Letterhead -->
  <div class="letterhead-underlay"></div>
  <section class="piece letterhead" aria-label="Letterhead">
    <span class="corner corner-top"></span>
    <span class="corner corner-bottom"></span>
    <div class="wordmark">Garnet<br>Words</div>
    <div class="sender">Alder Lane<br>Brookmere Court 12-408<br>7134620</div>
    <div class="body">
      <p class="salutation">Lorem ipsum</p>
      <p>Veniam dolorem democritum ei vis. Adhuc dolores offendit sea ne, qui no vitae iudico sanctus, accommodare consequuntur cu duo. Ut pro nulla oblique ponderum, viderer dolorum his et, vim adhuc ubique fuisset no. Qui reque explicari accusamus in.</p>
      <p>Te utamur interpretaris ius. Eu sed quidam utamur, soluta legendos deserunt in vel. Nam no dolorem eloquentiam, eum aliquam phaedrum consulatu ea. Sale iusto laoreet an quo, eos animal tibique et. Lorem electram et sea.</p>
      <p>Vero ceteros abhorreant et has, diam sonet delicata ex pro. Fabellas consulatu conceptam te eum, est congue rationibus incorrupte ea. Erat inani eu has, minim ubique assentior ut eos.</p>
      <p>Nibh aeterno eu nec, hinc elit tota et eos. Nec aliquid feugait probatus ad. Mei accusamus honestatis interesset in, ex brute iusto disputationi eam, simul nostrud maiestatis per ei.</p>
    </div>
    <div class="signer">Clara Vostell</div>
    <div class="signature" role="img" aria-label="Handwritten signature of Clara Vostell"></div>
    <div class="footer"><span>Company Address</span><span>hello@garnetwords.com</span><span>5550-3142</span></div>
  </section>

  <!-- CD -->
  <div class="disc" aria-label="CD label">
    <svg width="222" height="222" viewBox="0 0 222 222">
      <defs><clipPath id="disc-clip"><circle cx="111" cy="111" r="111"/></clipPath></defs>
      <g clip-path="url(#disc-clip)">
        <rect width="222" height="222" fill="var(--paper)"/>
        <rect y="123" width="222" height="99" fill="var(--brand-blue)" role="img" aria-label="Brand illustration area"/>
      </g>
      <circle cx="111" cy="111" r="39" fill="var(--disc-grey)"/>
      <circle cx="111" cy="111" r="12" fill="var(--backdrop)"/>
    </svg>
    <div class="wordmark">Garnet<br>Words</div>
  </div>

  <!-- CD sleeve -->
  <section class="piece sleeve" aria-label="CD sleeve">
    <span class="top-rule"></span>
    <div class="wordmark">Garnet<br>Words</div>
    <span class="bottom-band"></span>
  </section>

</body>
</html>
```